Alternative Country Rock Band Needs Website Design

Milo Q and The Drifthands Web Design Proposal

Overview
We essentially need design and code for an uncluttered, easy to navigate, simple to access repository for our music, videos, photos, up and coming shows, merchandise, and links to social media. It will be a platform for our fans, new and old to get to the heart of who we are and what we are doing. We want something that will embody our essence as musicians, our distinct flavor, and values. We must be able to add, remove and edit content without developer help.

*If we receive a design so good that it justifies no code, we are open to that*

Pagebook
It would be nice to have Pagebook integration so that much of the site can be liked, possibly commented on but most importantly shared.

This could also possibly be done on Blipper http://www.blipper-posts.example/ which posts right to Chirpline feeds and Pagebook with cross links back.

Smart Phone
We need the site to be compatible with smart phones.

Branding/Aesthetics

We are really keen on aesthetics. We are almost more concerned about the feel of the site than content, which of course will be there.

We want to aim at an edgy, gritty, folky rock ‘n’ roll with a cowboy kick ambiance. We want the space to have a Southwestern romanticism risqué tinge. We want something that feels similar to our new EP album cover “Dust On Gold.”

Our image is huge and we want people, agents, managers, venues, friends, family, and fans to see who we are immediately and be able to easily connect to us, share us, and contact us.

Content

Our EchoDistrict and Pagebook already exists, so much of it can essentially be reworked into the new site.

We want an About; Shows; Music; Videos (maybe combine as just “Music” so that we don’t clutter the site); Photos; Media/Press (one of the two); Store; Contact Us (booking inquiries etc.) and Easy Big Connectors to Social Media; Email List (somewhere, probably not in navigation)

Examples

These are band sites that we think more or less hit the nail on the head. When reviewing them, it seems we are drawn to sites that have very large pictures, large, easy to use navigation buttons and such.

http://sampletrackmusic.example/

http://www.norvalehollow.example/

http://thegreyheron.example/

http://www.cindermoonband.example/site/

http://www.theroamingkeys.example/ (love the size of the photos but don’t like the small navigation)

Hosting
Nimbusly has been recommended and it is free, but let us know if you know a better one.

Content Management
We want to be able to upload our shows using EchoDistrict and that they will show on our website, likely by using an RSS Feed. It might even be nice if music, photos and videos could also be linked. Basic Ruby on Rails has been recommended for content management, making it easier to add and remove content, but maybe you know better.

However, we are open to Pixel Yard or Qor as a prefabricated content management system as well.

Latest Technologies
We need the site up to date with the latest technologies out there, rss feeds, and so on so it will show up on search engines.

Project Deadline Extended
Reason: A number of designers accepted the job and are yet to submit their work.

Project Deadline Extended
Reason: We are looking for some original design elements. It seems many have over utilized our pictures to supplement design. We've added another $200 on top of the original $300 for a total of $500 for the project. We look forward to your participation!

We've added $200 to bring the total to $500 for our web design.  We are looking forward to your ideas...

Hi Designers,

We've added some more band pictures and posters for inspiration for possible designs.  We look forward to your submissions!

Milo Q

Store

Sans Serif
Decorative

```html
<!DOCTYPE html>
<html lang="en">
<head>
<meta charset="utf-8">
<title>About — Milo Q and The Drifthands</title>
<link rel="stylesheet" href="https://fonts.googleapis.com/css2?family=Bebas+Neue&family=Open+Sans:wght@400;600&display=swap">
<style>
  :root {
    --bar-dark: #221d18;
    --bar-edge: #3a332c;
    --nav-text: #c9c2b8;
    --nav-active-bg: #0b0a09;
    --nav-active-text: #ffffff;
    --parchment-light: #f3dcae;
    --parchment-mid: #e2b774;
    --parchment-deep: #b8733a;
    --panel: rgba(255, 250, 242, 0.86);
    --panel-rule: #e2c08e;
    --heading: #7a746e;
    --body-text: #3d3833;
    --footer-link: #5d554c;
    --photo-tone: #8d8a85;
    --square: #6b6258;
  }
  * { margin: 0; padding: 0; box-sizing: border-box; }
  html, body { width: 1200px; height: 933px; overflow: hidden; }
  body {
    position: relative;
    font-family: "Open Sans", Arial, sans-serif;
    background: var(--parchment-mid);
  }
  .backdrop {
    position: absolute; inset: 0;
    background:
      radial-gradient(ellipse 520px 420px at 560px 470px, rgba(255,246,225,.75), transparent 70%),
      radial-gradient(ellipse 900px 700px at 600px 450px, var(--parchment-light), var(--parchment-mid) 60%, var(--parchment-deep) 100%);
  }
  .site-header {
    position: absolute; left: 0; top: 0; width: 1200px; height: 71px;
    background: linear-gradient(var(--bar-edge), var(--bar-dark));
    border-bottom: 1px solid #14110e;
  }
  .main-nav {
    position: absolute; right: 72px; top: 2px; height: 69px;
    display: flex; list-style: none;
  }
  .main-nav li a {
    display: block; height: 69px; line-height: 69px;
    padding: 0 19px;
    font-family: "Bebas Neue", Impact, sans-serif;
    font-size: 21px; letter-spacing: .3px;
    color: var(--nav-text); text-decoration: none;
  }
  .main-nav li.store a { margin-left: 22px; }
  .main-nav li.is-active a { background: var(--nav-active-bg); color: var(--nav-active-text); }
  .page-title {
    position: absolute; left: 85px; top: 123px; width: 1019px; height: 62px;
    background: var(--panel);
    border-bottom: 4px solid var(--panel-rule);
  }
  .page-title h1 {
    font-family: "Bebas Neue", Impact, sans-serif; font-weight: 400;
    font-size: 31px; color: var(--heading);
    line-height: 62px; padding-left: 16px;
  }
  .content-panel {
    position: absolute; left: 85px; top: 191px; width: 1019px; height: 570px;
    background: var(--panel);
  }
  .band-photo {
    position: absolute; left: 93px; top: 23px; width: 833px; height: 304px;
    background: linear-gradient(180deg, #5f5d5a 0%, #a9a7a3 40%, var(--photo-tone) 70%, #6f6c68 100%);
  }
  .bio {
    position: absolute; left: 16px; top: 347px; width: 980px;
    font-size: 13.2px; line-height: 21px; color: var(--body-text);
  }
  .site-footer {
    position: absolute; left: 0; top: 889px; width: 1200px; height: 44px;
    background: var(--bar-dark);
    border-top: 3px solid #f5efe6;
  }
  .footer-nav {
    position: absolute; left: 85px; top: 11px;
    font-size: 13px; color: var(--footer-link);
  }
  .footer-nav a { color: var(--footer-link); text-decoration: none; }
  .social {
    position: absolute; right: 96px; top: 11px;
    display: flex; gap: 12px; list-style: none;
  }
  .social li { display: flex; align-items: center; gap: 4px; font-size: 12px; color: var(--nav-text); }
  .social li::before { content: ""; width: 10px; height: 10px; background: var(--square); }
</style>
</head>
<body>
  <div class="backdrop" role="img" aria-label="Worn parchment texture with a faint cowgirl figure and the Dust On Gold album artwork"></div>

  <header class="site-header">
    <ul class="main-nav">
      <li><a href="#">Home</a></li>
      <li class="is-active"><a href="#">About</a></li>
      <li><a href="#">Shows</a></li>
      <li><a href="#">Media/Press</a></li>
      <li class="store"><a href="#">Store</a></li>
      <li><a href="#">Contact Us</a></li>
    </ul>
  </header>

  <div class="page-title"><h1>About</h1></div>

  <main class="content-panel">
    <div class="band-photo" role="img" aria-label="Black and white photo of the six band members leaning on a wooden ranch fence"></div>
    <p class="bio">&nbsp;Milo Q and The Drifthands, of Southern California, deliver heartfelt ballads and gritty grassroots rock ‘n’ roll with a cowboy kick. Their folky story-telling songs convey themes of love, politics, environmentalism, childhood imagination, and the rawness of humanity. The concept of the band came to Milo Quarrow (lead singer, guitarist, former bassist of Velvet Ditch) in a burst of songwriting during a break from his former band. Milo called upon old friends Cal Brennick (guitar, harmonica) and Professor Ivo Starling (bass), and enlisted Rudy Vance (drums, harmony vocals) to complete the new group. Brennick now shares lead guitar duties for The Drifthands with the multi-talented musician and music teacher Eli Marquez and the newest addition, Fretline Hall blues competition titleholder Wade Halloran. Together, these players meld Southwestern romanticism, cultural awareness, and rollicking good times to get audiences dancing and leave them hungry for more.</p>
  </main>

  <footer class="site-footer">
    <nav class="footer-nav">
      <a href="#">Home</a> | <a href="#">About</a> | <a href="#">Shows</a> | <a href="#">Media/Press</a> | <a href="#">Store</a> | <a href="#">Contact Us</a>
    </nav>
    <ul class="social">
      <li>Pagebook</li>
      <li>Chirpline</li>
      <li>Orbitplus</li>
      <li>Snapfield</li>
    </ul>
  </footer>
</body>
</html>
```